Guaranteed Job - Sleek Sexy Business Card UV Spot

Im looking for a sleek and sexy business card, that resembles elite or VIP status status.
our business is corinvale.example
you can view our products on there, but our main audience for handing out our cards will be for people in the hospitality industry, so it will need to impress high management and CEO of hotels and restaurants, bars, clubs etc...
the card features will have UV spot on both sides, 400gsm stock. standard size.
Artwork should be 86 x 54mm + 2mm bleed = 90 x 58mm
it should have a nice "unique" uv spot pattern that highlights the card, not a repeated pattern, theres no originality there, and it will be disregarded.
The written material will be:
Corin Vale Hospitality College (logo)
Tobin Marsh
Director
Phone: 1300 615 737
Mobile: 0455 817 296
Email: info@corinvale.example
website: www.corinvale.example
I'm looking for originality here, i don't want just a simple stock card, want something that has a wow factor for people.
You will find the logo attached. you may invert the white to black words to suit the background as you please.
thank you and good luck
As a side note, ive received a lot of proposals, im too busy to give feedback to each and every one, so if i havent provided feedback for your design within 24 hours, then consider it not acceptable, and you could resubmit another design.
So far i have not seen any design that stood out for me, they all seem pretty generic. there nothing thats unique, i would figure for the amount that im offering, that people would put some more effort and creativity into the design.
so far over 200 designs submitted, and nothing i have seen looks very original, everything looks like a different variation of the same stuff, i said it very clearly i wanted something unique, the only thing that has come close to it so far is this one
Reason: Ive received alot of design concepts and i have reviewed everyone, but i havent had time to give feedback to every single one, only the ones that have interested me, if i havent responded, its because i havent found it good enough.
so far only a few design have been on par with what ive been looking for, an attractive eye popping design.
heres a few of them,
http://files.pixelbazaar.example/design_img/51736/62418/62418_2840915_51736_image.jpg
http://files.pixelbazaar.example/design_img/51736/68254/68254_2841377_51736_image.jpg
theyre, both unique and original, and eye catching, the only thing theyre missing is the sexyness.
if you still think you have some creativity left in your minds, then throw it on here.
Reason: Sorry guys for the delay, I was in a serious accident and out of commission for the past few months, I'm just slowly recovering now, please bare with me as i try to attend to this project, it may take me awhile as I have other projects that are on standby, I'm not 100% at the moment, so im extending the deadline for 2 weeks right now. Thanks for your patience.
Hospitality

```html
<!DOCTYPE html>
<html lang="en">
<head>
<meta charset="utf-8">
<title>Corin Vale Hospitality College – Business Card</title>
<link rel="stylesheet" href="https://fonts.googleapis.com/css2?family=Barlow+Semi+Condensed:wght@600&family=Arimo&display=swap">
<style>
  :root {
    --page: #ffffff;
    --label: #1a1a1a;
    --card-front: #231f20;
    --card-back: #2a2929;
    --stripe-front: #ffffff;
    --stripe-back: #5c5c5c;
    --name-front: #ffffff;
    --name-back: #4f4f4f;
    --accent-front: #4ba3dc;
    --accent-back: #2f4561;
    --contact-front: #ffffff;
    --contact-back: #555555;
  }
  html, body {
    margin: 0;
    padding: 0;
    width: 1200px;
    height: 1200px;
    overflow: hidden;
    background: var(--page);
  }
  .sheet {
    position: relative;
    width: 1200px;
    height: 1200px;
  }
  .side-label {
    position: absolute;
    left: 247px;
    margin: 0;
    font-family: "Arimo", Arial, sans-serif;
    font-size: 24px;
    font-weight: 400;
    color: var(--label);
  }
  .side-label--front { top: 96px; }
  .side-label--back { top: 673px; }

  .card {
    position: absolute;
    left: 244px;
    width: 708px;
    height: 395px;
    overflow: hidden;
  }
  .card--front { top: 133px; background: var(--card-front); }
  .card--back { top: 703px; background: var(--card-back); }

  .card__layout {
    position: absolute;
    inset: 0;
  }
  .card--back .card__layout { transform: scaleX(-1); }

  .card__stripe {
    position: absolute;
    inset: 0;
    width: 708px;
    height: 395px;
  }
  .card--front .card__stripe polygon { fill: var(--stripe-front); }
  .card--back .card__stripe polygon { fill: var(--stripe-back); }

  .brand__square {
    position: absolute;
    left: 72px;
    top: 66px;
    width: 112px;
    height: 112px;
  }
  .card--front .brand__square { background: var(--accent-front); }
  .card--back .brand__square { background: var(--accent-back); }

  .brand__name {
    position: absolute;
    left: 226px;
    top: 76px;
    margin: 0;
    font-family: "Barlow Semi Condensed", "Arial Narrow", sans-serif;
    font-weight: 600;
    text-transform: uppercase;
    line-height: 1;
  }
  .card--front .brand__name { color: var(--name-front); }
  .card--back .brand__name { color: var(--name-back); }
  .brand__line { display: block; }
  .brand__line--top { font-size: 46px; letter-spacing: 1px; }
  .brand__line--main { font-size: 50px; letter-spacing: 1px; margin-top: 2px; }
  .brand__line--sub { font-size: 19px; letter-spacing: 1.6px; margin-top: 8px; }

  .contact {
    position: absolute;
    left: 86px;
    top: 252px;
    margin: 0;
    font-family: "Arimo", Arial, sans-serif;
    font-size: 16px;
    line-height: 18.6px;
    font-style: normal;
  }
  .card--front .contact { color: var(--contact-front); }
  .card--back .contact { color: var(--contact-back); }
  .contact span { display: block; }
</style>
</head>
<body>
<main class="sheet">
  <p class="side-label side-label--front">front side</p>
  <section class="card card--front" aria-label="Business card, front side">
    <div class="card__layout">
      <svg class="card__stripe" viewBox="0 0 708 395" aria-hidden="true">
        <polygon points="708,0 390,395 486,395"/>
      </svg>
      <div class="brand__square" aria-hidden="true"></div>
      <h1 class="brand__name">
        <span class="brand__line brand__line--top">Corin</span>
        <span class="brand__line brand__line--main">Vale</span>
        <span class="brand__line brand__line--sub">Hospitality College</span>
      </h1>
      <address class="contact">
        <span>Tobin Marsh</span>
        <span>Director</span>
        <span>Phone: 1300 615 737</span>
        <span>Mobile: 0455 817 296</span>
        <span>Email: info@corinvale.example</span>
        <span>website: www.corinvale.example</span>
      </address>
    </div>
  </section>

  <p class="side-label side-label--back">back side</p>
  <section class="card card--back" aria-label="Business card, back side">
    <div class="card__layout">
      <svg class="card__stripe" viewBox="0 0 708 395" aria-hidden="true">
        <polygon points="708,0 388,395 531,395"/>
      </svg>
      <div class="brand__square" aria-hidden="true"></div>
      <p class="brand__name">
        <span class="brand__line brand__line--top">Corin</span>
        <span class="brand__line brand__line--main">Vale</span>
        <span class="brand__line brand__line--sub">Hospitality College</span>
      </p>
      <address class="contact">
        <span>Tobin Marsh</span>
        <span>Director</span>
        <span>Phone: 1300 615 737</span>
        <span>Mobile: 0455 817 296</span>
        <span>Email: info@corinvale.example</span>
        <span>website: www.corinvale.example</span>
      </address>
    </div>
  </section>
</main>
</body>
</html>
```